Moravel Stenwick Inc needs a business card design

Looking for a unique, classy and sharp business card design.

Contact Information for Business Card

Moravel Stenwick Inc.
Marisa Ortega Bellido BScOT(c)
Occupational Therapist
(780) 555-0142
moravelstenwick@postlynx.net

```html
<!DOCTYPE html>
<html lang="en">
<head>
<meta charset="utf-8">
<title>Moravel Stenwick Inc. – Business Card</title>
<link href="https://fonts.googleapis.com/css2?family=Source+Sans+3:wght@400;600&display=swap" rel="stylesheet">
<style>
  :root {
    --backdrop: #3b3430;
    --card: #0d0d0d;
    --card-edge: #1c1c1c;
    --purple: #a03fa8;
    --green: #8cc63f;
    --blue: #29a9e0;
    --text: #e6e6e6;
    --silver: #cfcfcf;
    --divider: #262626;
  }
  * { box-sizing: border-box; margin: 0; padding: 0; }
  html, body { width: 1200px; height: 844px; overflow: hidden; }
  body {
    background: var(--backdrop);
    font-family: "Source Sans 3", "Myriad Pro", Arial, sans-serif;
    position: relative;
  }
  .card {
    position: absolute;
    top: 272px;
    width: 520px;
    height: 300px;
    background: var(--card);
    border: 1px solid var(--card-edge);
    box-shadow: 0 14px 30px rgba(0,0,0,.45);
  }
  .card--front { left: 50px; }
  .card--back { left: 630px; display: flex; align-items: center; justify-content: center; }

  .brand-slot {
    position: absolute;
    left: 0; top: 0;
    width: 180px; height: 100%;
    display: flex; flex-direction: column;
    align-items: center; justify-content: center;
    gap: 10px;
  }
  .brand-slot__dot {
    width: 48px; height: 48px; border-radius: 50%;
    background: var(--green);
  }
  .brand-slot__name {
    font-size: 13px; font-weight: 600; color: var(--text);
    text-align: center; line-height: 1.2;
  }
  .divider {
    position: absolute; left: 180px; top: 40px; bottom: 40px;
    width: 1px; background: var(--divider);
  }
  .details { position: absolute; left: 205px; top: 78px; }
  .person-name { font-size: 21px; font-weight: 600; white-space: nowrap; }
  .person-name__first { color: var(--purple); }
  .person-name__last { color: var(--green); }
  .person-name__cred { color: var(--green); font-size: 14px; }
  .person-role { color: var(--text); font-size: 14px; margin-top: 2px; }
  .contact { list-style: none; margin-top: 28px; }
  .contact li {
    display: flex; align-items: center; gap: 8px;
    color: var(--text); font-size: 14px; line-height: 22px;
  }
  .contact svg { width: 11px; height: 11px; fill: var(--green); flex: none; }

  .back-brand {
    font-size: 38px; font-weight: 600; color: var(--silver);
    letter-spacing: .5px;
  }
</style>
</head>
<body>
  <section class="card card--front" aria-label="Business card front">
    <div class="brand-slot">
      <span class="brand-slot__dot"></span>
      <span class="brand-slot__name">Moravel Stenwick Inc.</span>
    </div>
    <div class="divider"></div>
    <div class="details">
      <p class="person-name">
        <span class="person-name__first">Marisa Ortega</span>
        <span class="person-name__last">Bellido</span>
        <span class="person-name__cred">BScOT(c)</span>
      </p>
      <p class="person-role">Occupational Therapist</p>
      <ul class="contact">
        <li>
          <svg viewBox="0 0 24 24" aria-hidden="true"><path d="M6.6 10.8a15.1 15.1 0 0 0 6.6 6.6l2.2-2.2a1 1 0 0 1 1-.25 11.4 11.4 0 0 0 3.6.57 1 1 0 0 1 1 1V20a1 1 0 0 1-1 1A17 17 0 0 1 3 4a1 1 0 0 1 1-1h3.5a1 1 0 0 1 1 1c0 1.25.2 2.45.57 3.6a1 1 0 0 1-.25 1z"/></svg>
          (780) 555-0142
        </li>
        <li>
          <svg viewBox="0 0 24 24" aria-hidden="true"><path d="M2 5h20v14H2z M2 5l10 7 10-7" fill="none" stroke="#8cc63f" stroke-width="0"/><path d="M2 5h20v2l-10 6L2 7z M2 9l10 6 10-6v10H2z"/></svg>
          moravelstenwick@postlynx.net
        </li>
      </ul>
    </div>
  </section>

  <section class="card card--back" aria-label="Business card back">
    <p class="back-brand">Moravel Stenwick Inc.</p>
  </section>
</body>
</html>
```